Kelp Pocket Apps Needs banners for webpage

We need a top banner. We are a mobile app developer for the Hospitality Industry. We are developing a Loyalty Program with the trade name KelpPerks. The banner will be used on our loyalty page inside our website.Please see www.kelppocketapps.example to understand our theme. The banner should be 1700 X 470.

Please see the attached banner. This is from a competitor website.Please use it as a model and make changes...... make it unique to KelpPocket. I need to convey the same message as this banner. Same statistics. Same setting (restaurant).

I have added a purchased vector file for the restaurant setting. I noticed many are struggling and using stock art which I don't like.Work with the background color. Make it more playful--pastels--less formal. Be creative!

Do not wait till that last day of the contest to submit. I might take the first design I like and proceed. The sooner you post a design, the better direction I can give you.
Updates

Reason: Not getting any designs I can work with yet. Please give me ideas.

All, Please re-read the brief. I have changed the banner project. It will be much easier but I need it quickly.

Now that I have made this banner much easier, I would like to wrap this contest up. Don't wait till the last day to post designs. The first design I like I will go with and close the project. Be creative, colorful, imaginative! Good luck. Martin Orrey Kelp Pocket Apps, LLC morrey@

All. See the vector file that I just purchased for the background image. Can you try different background colors. I still need the other content showing the percentages of loyalty. I do not want the rocket ship!

All, I have updated the brief. I have included a vector file that has a perfect restaurant scene. Please be creative and work with colors in this scene. Also be creative with the information in the circles showing the metrics of loyalty. Do not use the Rocket. If you find another idea to replace the rocket, that's fine. Or, just leave it off. Please make this banner unique!

Target Market(s)

Hospitality Industry.

Industry/Entity Type

Restaurant

Requirements
Must have
• Banner should be beautiful.. Image of diners at restaurant along with the statistics and message "Boost Sales".
Nice to have
• Our banner should convey the same message as the attached but we must re-design because the attached banner belongs to another company.
Should not have
• Do not re-use any of the images in the attached banner. This is from my competitor. Do not use a rocket for "Boost Sales" image.

```html
<!DOCTYPE html>
<html lang="en">
<head>
<meta charset="utf-8">
<title>Boost Sales – KelpPerks Loyalty Banner</title>
<link href="https://fonts.googleapis.com/css2?family=Great+Vibes&family=Oswald:wght@400;500&family=Roboto+Condensed:wght@400;700&display=swap" rel="stylesheet">
<style>
  :root {
    --scene-peach: #f7d2c4;
    --scene-rose: #eebfd3;
    --scene-lavender: #cdbde9;
    --scene-mint: #c6e8dc;
    --diner-white: #ffffff;
    --headline-coral: #d9664f;
    --headline-peach: #f29a74;
    --caption-bg: #4a3f63;
    --caption-text: #ffffff;
    --star: #f2a65a;
    --badge-fill: #3f3658;
    --badge-ring: #8f84b3;
    --badge-text: #d9d2ee;
    --accent: #ffb27a;
    --icon-soft: #bfe3d6;
  }
  * { margin: 0; padding: 0; box-sizing: border-box; }
  html, body { width: 1200px; height: 331px; overflow: hidden; background: var(--diner-white); }

  .banner {
    position: relative;
    width: 1200px;
    height: 331px;
    overflow: hidden;
  }

  .restaurant-scene {
    position: absolute;
    inset: 0;
    background:
      linear-gradient(180deg, rgba(255,255,255,0) 0%, rgba(255,255,255,0) 52%, rgba(255,255,255,0.7) 78%, var(--diner-white) 96%),
      radial-gradient(ellipse at 18% 30%, var(--scene-mint) 0%, rgba(198,232,220,0) 45%),
      radial-gradient(ellipse at 82% 30%, var(--scene-lavender) 0%, rgba(205,189,233,0) 50%),
      linear-gradient(90deg, var(--scene-peach) 0%, var(--scene-rose) 50%, var(--scene-lavender) 100%);
  }

  .headline {
    position: absolute;
    top: 12px;
    left: 0;
    width: 100%;
    text-align: center;
  }
  .headline-title {
    font-family: "Great Vibes", cursive;
    font-weight: 400;
    font-size: 62px;
    line-height: 1;
    color: var(--headline-coral);
    background: linear-gradient(180deg, var(--headline-peach), var(--headline-coral));
    -webkit-background-clip: text;
    background-clip: text;
    -webkit-text-fill-color: transparent;
  }
  .headline-caption {
    display: inline-flex;
    align-items: center;
    gap: 10px;
    margin-top: 2px;
  }
  .caption-star { width: 11px; height: 11px; fill: var(--star); }
  .caption-label {
    font-family: "Oswald", sans-serif;
    font-weight: 400;
    font-size: 18px;
    letter-spacing: 0.3px;
    color: var(--caption-text);
    background: var(--caption-bg);
    border-top: 1px solid rgba(255,255,255,0.8);
    border-bottom: 1px solid rgba(255,255,255,0.8);
    padding: 1px 8px;
    line-height: 1.25;
  }

  .stat-badge {
    position: absolute;
    top: 176px;
    width: 130px;
    height: 130px;
  }
  .stat-badge--visits { left: 300px; }
  .stat-badge--spend  { left: 532px; }
  .stat-badge--ratio  { left: 766px; }

  .badge-arc-text {
    font-family: "Roboto Condensed", sans-serif;
    font-size: 10px;
    letter-spacing: 0.6px;
    fill: var(--badge-text);
  }
  .badge-arc-text .highlight { fill: var(--accent); font-weight: 700; }
  .badge-figure {
    font-family: "Oswald", sans-serif;
    font-weight: 500;
    font-size: 40px;
    fill: var(--accent);
  }
</style>
</head>
<body>
<div class="banner">
  <div class="restaurant-scene" role="img" aria-label="Pastel restaurant scene with white silhouettes of diners at tables and a waiter carrying a tray"></div>

  <header class="headline">
    <h1 class="headline-title">Boost Sales</h1>
    <div class="headline-caption">
      <svg class="caption-star" viewBox="0 0 10 10"><polygon points="5,0 6.2,3.6 10,3.6 6.9,5.8 8.1,9.5 5,7.2 1.9,9.5 3.1,5.8 0,3.6 3.8,3.6"/></svg>
      <span class="caption-label">CAPTION HERE</span>
      <svg class="caption-star" viewBox="0 0 10 10"><polygon points="5,0 6.2,3.6 10,3.6 6.9,5.8 8.1,9.5 5,7.2 1.9,9.5 3.1,5.8 0,3.6 3.8,3.6"/></svg>
    </div>
  </header>

  <svg width="0" height="0" style="position:absolute">
    <defs>
      <path id="arc-top" d="M 22,80 A 58,58 0 0 1 138,80"/>
      <path id="arc-bottom" d="M 15,80 A 65,65 0 0 0 145,80"/>
      <symbol id="person-icon" viewBox="0 0 10 20">
        <circle cx="5" cy="3" r="2.6"/>
        <rect x="1.5" y="6.3" width="7" height="7" rx="1.2"/>
        <rect x="2.2" y="12.5" width="2.3" height="7"/>
        <rect x="5.5" y="12.5" width="2.3" height="7"/>
      </symbol>
    </defs>
  </svg>

  <svg class="stat-badge stat-badge--visits" viewBox="0 0 160 160" aria-label="Loyal guests visit about 32% more than average guests">
    <circle cx="80" cy="80" r="80" fill="var(--badge-fill)"/>
    <circle cx="80" cy="80" r="72" fill="none" stroke="var(--badge-ring)" stroke-width="1.2"/>
    <circle cx="80" cy="80" r="48" fill="none" stroke="var(--badge-ring)" stroke-width="1.2"/>
    <text class="badge-arc-text"><textPath href="#arc-top" startOffset="50%" text-anchor="middle">LOYEL GUESTS VISITS ABOUT</textPath></text>
    <text class="badge-arc-text"><textPath href="#arc-bottom" startOffset="50%" text-anchor="middle">MORE THAN AVERAGE GUESTS</textPath></text>
    <text class="badge-figure" x="80" y="95" text-anchor="middle">32%</text>
  </svg>

  <svg class="stat-badge stat-badge--spend" viewBox="0 0 160 160" aria-label="Loyal guests spend about 22% more than average guests">
    <circle cx="80" cy="80" r="80" fill="var(--badge-fill)"/>
    <circle cx="80" cy="80" r="72" fill="none" stroke="var(--badge-ring)" stroke-width="1.2"/>
    <circle cx="80" cy="80" r="48" fill="none" stroke="var(--badge-ring)" stroke-width="1.2"/>
    <text class="badge-arc-text"><textPath href="#arc-top" startOffset="50%" text-anchor="middle">LOYEL GUESTS SPEND ABOUT</textPath></text>
    <text class="badge-arc-text"><textPath href="#arc-bottom" startOffset="50%" text-anchor="middle">MORE THAN AVERAGE GUESTS</textPath></text>
    <text class="badge-figure" x="80" y="95" text-anchor="middle">22%</text>
  </svg>

  <svg class="stat-badge stat-badge--ratio" viewBox="0 0 160 160" aria-label="One loyal guest equals ten average guests">
    <circle cx="80" cy="80" r="80" fill="var(--badge-fill)"/>
    <circle cx="80" cy="80" r="72" fill="none" stroke="var(--badge-ring)" stroke-width="1.2"/>
    <text class="badge-arc-text"><textPath href="#arc-top" startOffset="50%" text-anchor="middle"><tspan class="highlight">ONE</tspan> LOYEL GUESTS =</textPath></text>
    <text class="badge-arc-text"><textPath href="#arc-bottom" startOffset="50%" text-anchor="middle"><tspan class="highlight">TEN</tspan> AVERAGE GUESTS</textPath></text>
    <g fill="var(--accent)">
      <use href="#person-icon" x="74" y="38" width="12" height="24"/>
    </g>
    <g fill="var(--icon-soft)">
      <use href="#person-icon" x="49" y="70" width="9" height="18"/>
      <use href="#person-icon" x="60" y="70" width="9" height="18"/>
      <use href="#person-icon" x="71" y="70" width="9" height="18"/>
      <use href="#person-icon" x="82" y="70" width="9" height="18"/>
      <use href="#person-icon" x="93" y="70" width="9" height="18"/>
      <use href="#person-icon" x="104" y="70" width="9" height="18"/>
      <use href="#person-icon" x="60" y="92" width="9" height="18"/>
      <use href="#person-icon" x="71" y="92" width="9" height="18"/>
      <use href="#person-icon" x="82" y="92" width="9" height="18"/>
      <use href="#person-icon" x="93" y="92" width="9" height="18"/>
    </g>
  </svg>
</div>
</body>
</html>
```